MD Trailcraft & Wildland Expo

I need a 1 page flyer for promotion of an upcoming sportsman and outdoor show(expo). would like the flyer to be able to be printed in B&W and color! show will include all things to do with the out doors, hunting fishing boating hiking atv camping rvs motorcycles. the event will have a kids zone, events games and activities for kids. there will be vendors showing the newest products. guest speakers and industry experts giving training and advice. this show will have something for everyone. food trucks and concessions. 200+ vendors. waterfould calling competition. deer/buck scoring casting competition for kids 3D Archery competitions

Target Market(s)

anyone event open to all ages!

Colors
ec1f27
000000
fbed22

Requirements
Must have
• date- september 1-2 2018
• location Penwick county fair 4817 millbrook rd east caldon MD 21638
• facebook - mdtrailcraftexpo
• email mdtrailcraftexpo@mailvento.com
• web www.mdtrailcraftexpo-demo.com
• vendor spaces still available! sign up now space going fast
Nice to have
• would like some thing that can be both printed in B&W and Color, and still have a great affect.
Should not have
• open to any suggestions

```html
<!DOCTYPE html>
<html lang="en">
<head>
<meta charset="utf-8">
<title>MD Trailcraft &amp; Wildland Expo — Flyer</title>
<link href="https://fonts.googleapis.com/css2?family=Cabin:wght@400;600;700&family=Roboto+Slab:wght@700;800;900&display=swap" rel="stylesheet">
<style>
  :root{
    --red:#ec1f27;
    --black:#000000;
    --white:#ffffff;
    --page:#e9e9e9;
    --ink:#1a1a1a;
  }
  *{margin:0;padding:0;box-sizing:border-box}
  html,body{width:1200px;height:1200px;overflow:hidden;background:var(--page)}
  .flyer{
    position:absolute;left:190px;top:25px;width:923px;height:1296px;
    transform:scale(0.8873);transform-origin:0 0;
    background:var(--black);overflow:hidden;
    font-family:"Cabin",Arial,sans-serif;
  }
  .shapes{position:absolute;inset:0;width:923px;height:1296px}
  .title{
    position:absolute;left:440px;top:22px;width:483px;text-align:center;
    font-family:"Roboto Slab",Georgia,serif;font-weight:900;color:var(--white);
    font-size:44px;line-height:54px;text-transform:uppercase;
  }
  .date{
    position:absolute;left:440px;top:160px;width:483px;text-align:center;
    font-family:"Roboto Slab",Georgia,serif;font-weight:900;color:var(--white);
    font-size:44px;line-height:52px;
  }
  .banner-text{
    position:absolute;left:392px;top:482px;width:515px;text-align:right;
    font-family:"Roboto Slab",Georgia,serif;font-weight:800;color:var(--white);
    font-size:20px;line-height:29px;
  }
  .offer-list{position:absolute;left:378px;top:571px;list-style:none;width:530px;height:280px}
  .offer-list li{
    position:absolute;color:var(--white);font-size:16.5px;line-height:20px;padding-left:16px;
  }
  .offer-list li::before{
    content:"";position:absolute;left:0;top:7px;width:8px;height:8px;border-radius:50%;background:var(--red);
  }
  .about-block{position:absolute;left:0;top:902px;width:892px;height:232px}
  .about-block .slant{
    float:left;width:480px;height:232px;
    shape-outside:polygon(0 0,365px 0,475px 232px,0 232px);
  }
  .about{
    color:var(--white);font-size:19px;line-height:23.6px;
    text-align:justify;text-align-last:right;
  }
  .cta{
    position:absolute;left:0;top:1172px;width:923px;text-align:center;color:var(--red);
    font-size:28px;
  }
  .cta strong{font-weight:700}
  .contact{position:absolute;color:var(--ink);font-size:15.5px;line-height:20px}
  .contact svg{position:absolute;left:-30px;top:0}
  .address{left:52px;top:1224px;width:290px}
  .email{left:412px;top:1220px}
  .web{left:678px;top:1220px}
  .social{left:412px;top:1249px}
</style>
</head>
<body>
<main class="flyer">
  <svg class="shapes" viewBox="0 0 923 1296">
    <defs>
      <linearGradient id="sunset" x1="0" y1="0" x2="0.4" y2="1">
        <stop offset="0" stop-color="#3f7fa3"/><stop offset="0.45" stop-color="#c9c1a0"/>
        <stop offset="0.62" stop-color="#e8a653"/><stop offset="1" stop-color="#3e3f45"/>
      </linearGradient>
      <linearGradient id="lake" x1="0" y1="0" x2="0" y2="1">
        <stop offset="0" stop-color="#b9cfe0"/><stop offset="0.3" stop-color="#3f6a2e"/>
        <stop offset="0.6" stop-color="#55763f"/><stop offset="1" stop-color="#2c5a8e"/>
      </linearGradient>
      <linearGradient id="trail" x1="0" y1="0" x2="1" y2="1">
        <stop offset="0" stop-color="#7ea3c6"/><stop offset="0.4" stop-color="#e3c98e"/>
        <stop offset="1" stop-color="#5a3c22"/>
      </linearGradient>
      <linearGradient id="kids" x1="0" y1="0" x2="1" y2="0">
        <stop offset="0" stop-color="#7b6a62"/><stop offset="0.5" stop-color="#9fc3d6"/>
        <stop offset="1" stop-color="#8a6f3d"/>
      </linearGradient>
    </defs>
    <polygon points="0,0 432,0 322,855 0,855" fill="var(--red)"/>
    <polygon points="452,0 923,0 923,153 432,153" fill="var(--red)"/>
    <polygon points="0,0 408,0 337,552 0,552" fill="var(--white)"/>
    <polygon points="0,0 404,0 334,548 0,548" fill="url(#sunset)" role="img" aria-label="Angler casting a rod from a boat at sunset"/>
    <polygon points="0,576 334,576 299,853 0,853" fill="var(--white)"/>
    <polygon points="0,580 329,580 295,849 0,849" fill="url(#trail)" role="img" aria-label="Hikers with backpacks walking a grassy trail"/>
    <polygon points="425,226 923,226 923,459 396,459" fill="var(--white)"/>
    <polygon points="429,230 923,230 923,455 401,455" fill="url(#lake)" role="img" aria-label="Rowing boat on a calm forest lake"/>
    <polygon points="392,478 923,478 923,545 382,545" fill="var(--red)"/>
    <rect x="0" y="855" width="923" height="18" fill="var(--red)"/>
    <polygon points="0,892 325,892 430,1124 0,1124" fill="var(--white)"/>
    <polygon points="0,896 322,896 424,1120 0,1120" fill="url(#kids)" role="img" aria-label="Children playing games in the kids zone"/>
    <rect x="0" y="1145" width="923" height="9" fill="var(--red)"/>
    <rect x="0" y="1154" width="923" height="142" fill="var(--white)"/>
  </svg>

  <h1 class="title">MD Trailcraft &amp;<br>Wildland Expo</h1>
  <p class="date">September 1-2, 2018</p>
  <p class="banner-text">Over 60,000 sqft of INDOOR and 30,000+ sqft<br>OUTDOOR products and services including:</p>

  <ul class="offer-list">
    <li style="left:0;top:0">Sports Equipment</li>
    <li style="left:163px;top:0">Campers</li>
    <li style="left:314px;top:0">Boats</li>
    <li style="left:430px;top:0">RV’s</li>
    <li style="left:0;top:45px">Tackle &amp; Bait</li>
    <li style="left:163px;top:45px">Motorcycles</li>
    <li style="left:314px;top:45px">ATV’s</li>
    <li style="left:430px;top:45px">Trucks</li>
    <li style="left:0;top:90px">Taxidermists</li>
    <li style="left:163px;top:90px">Outfitters</li>
    <li style="left:314px;top:90px">Guns</li>
    <li style="left:430px;top:90px">Jet Skis</li>
    <li style="left:0;top:135px">Charter Boats</li>
    <li style="left:163px;top:135px">Golf Resorts</li>
    <li style="left:314px;top:135px">Knives</li>
    <li style="left:430px;top:135px">Archery</li>
    <li style="left:0;top:180px">Trailers</li>
    <li style="left:163px;top:180px">Sporting Clubs</li>
    <li style="left:314px;top:180px">Game Calls</li>
    <li style="left:430px;top:180px">Outdoor<br>Magazines</li>
    <li style="left:0;top:225px">Camp Grounds</li>
    <li style="left:163px;top:225px">Camping<br>Equipment</li>
    <li style="left:314px;top:225px">Hunting<br>Supplies</li>
  </ul>

  <div class="about-block">
    <div class="slant"></div>
    <p class="about">The show will include all things to do with the out doors, hunting fishing, boating, hiking, atv camping, rvs motorcycles. the event will have a kids zone, events games and activities for kids. There will be vendors showing the newest products, guest speakers and industry experts giving training and advice, food trucks and concessions. 200+ vendors, waterfould calling competition, deer/buck scoring casting competition for kids 3D Archery competitions.</p>
  </div>

  <p class="cta">Vendors Spaces Still Available!<strong>Sign up now</strong> space going fast</p>

  <p class="contact address">
    <svg width="18" height="22" viewBox="0 0 18 22"><path d="M9 1a7 7 0 0 0-7 7c0 5 7 13 7 13s7-8 7-13a7 7 0 0 0-7-7z" fill="var(--red)"/><circle cx="9" cy="8" r="2.6" fill="var(--white)"/></svg>
    Penwick county fair 4817 millbrook<br>rd east caldon MD 21638
  </p>
  <p class="contact email">
    <svg width="20" height="16" viewBox="0 0 20 16" style="top:3px"><rect x="1" y="2" width="18" height="12" fill="var(--red)"/><path d="M1 2l9 7 9-7" fill="none" stroke="var(--white)" stroke-width="1.6"/></svg>
    mdtrailcraftexpo@mailvento.com
  </p>
  <p class="contact web">
    <svg width="20" height="20" viewBox="0 0 20 20"><circle cx="10" cy="10" r="8" fill="none" stroke="var(--red)" stroke-width="1.6"/><ellipse cx="10" cy="10" rx="3.5" ry="8" fill="none" stroke="var(--red)" stroke-width="1.4"/><path d="M2 10h16M3.5 6h13M3.5 14h13" stroke="var(--red)" stroke-width="1.3"/></svg>
    www.mdtrailcraftexpo-demo.com
  </p>
  <p class="contact social">
    <svg width="22" height="22" viewBox="0 0 22 22"><circle cx="11" cy="11" r="9.5" fill="none" stroke="var(--red)" stroke-width="1.6"/></svg>
    mdtrailcraftexpo
  </p>
</main>
</body>
</html>
```